Maple Hollow Elementary School Letterhead

We would like a letterhead that includes our school mascot (Bramble the Badger), school address, and phone number. We want something with personality and a little fun. Our school colors are navy blue, green (like the flag in our graphic), and gray. We included an example of a letterhead we like the feel of (on the fun side). The example is the image titled "sample." We are the Maple Hollow Badgers.
Maple Hollow Elementary
Address: 718 Dovetail Fern, Irvine, CA 92614
Phone: (949) 555-0147
maplehollow.qpsd-example.org

```html
<!DOCTYPE html>
<html lang="en">
<head>
<meta charset="utf-8">
<title>Maple Hollow Elementary Letterhead</title>
<link href="https://fonts.googleapis.com/css2?family=Montserrat:wght@500;700&family=Open+Sans:wght@400;600&family=Poppins:wght@400;700&family=Great+Vibes&display=swap" rel="stylesheet">
<style>
  :root {
    --navy: #1c4595;
    --green: #39a547;
    --charcoal: #444446;
    --ink: #2f2f35;
    --muted: #8b8b98;
    --label: #23408f;
    --backdrop: #ffffff;
    --paper: #ffffff;
  }
  * { margin: 0; padding: 0; box-sizing: border-box; }
  html, body { width: 1021px; height: 1200px; overflow: hidden; background: var(--backdrop); }
  .letterhead {
    position: absolute; left: 85px; top: 0;
    width: 860px; height: 1212px;
    background: var(--paper);
    transform: scale(0.9901); transform-origin: 0 0;
    overflow: hidden;
    font-family: "Poppins", sans-serif;
    box-shadow: 0 0 0 1px #eeeeee;
  }
  .header-art { position: absolute; left: 0; top: 0; width: 860px; height: 280px; }
  .footer-art { position: absolute; left: 0; top: 1012px; width: 860px; height: 200px; }

  .school-mark { position: absolute; left: 52px; top: 54px; display: flex; align-items: center; gap: 14px; color: #fff; font-family: "Poppins", sans-serif; font-weight: 700; }
  .school-mark .dot { width: 44px; height: 44px; border-radius: 50%; background: rgba(255,255,255,.25); }
  .school-mark .name { font-size: 34px; line-height: 1; letter-spacing: .5px; }
  .school-mark .sub { display: block; font-size: 13px; letter-spacing: 2px; margin-top: 6px; }

  .recipient { position: absolute; left: 64px; top: 246px; font-family: "Open Sans", sans-serif; color: var(--ink); font-size: 14px; line-height: 19px; }
  .recipient .to { display: block; }
  .recipient .name { display: block; font-family: "Montserrat", sans-serif; font-weight: 700; color: var(--label); font-size: 18px; letter-spacing: .6px; margin: 0 0 4px; }
  .recipient b { font-weight: 600; }

  .letter-date { position: absolute; right: 56px; top: 313px; font-family: "Open Sans", sans-serif; font-size: 13.5px; color: var(--ink); }
  .letter-date b { color: var(--label); font-family: "Montserrat", sans-serif; font-weight: 700; }

  .letter-body { position: absolute; left: 62px; top: 396px; width: 742px; font-size: 11.4px; line-height: 18.5px; color: var(--muted); text-align: justify; }
  .letter-body p { margin-bottom: 18px; }
  .letter-body p.strong { color: var(--ink); }

  .sign-off { position: absolute; left: 57px; top: 862px; width: 177px; }
  .sign-off .signature { height: 38px; background: linear-gradient(90deg, #f2f2f4, #e4e4e8); border-radius: 3px; }
  .sign-off .rule { height: 2px; background: var(--ink); margin-top: 2px; }
  .sign-off .designation { margin-top: 14px; padding-left: 8px; font-family: "Montserrat", sans-serif; font-weight: 700; font-size: 11px; letter-spacing: .8px; color: var(--ink); white-space: nowrap; }

  .footer-name { position: absolute; left: 58px; top: 1108px; font-family: "Great Vibes", cursive; font-size: 36px; color: #fff; }
  .contact { position: absolute; left: 577px; top: 1055px; font-family: "Open Sans", sans-serif; font-size: 11.5px; color: var(--ink); line-height: 23px; }
  .contact b { color: var(--label); font-weight: 600; }
  .contact .address { font-weight: 600; color: #111; }
</style>
</head>
<body>
<div class="letterhead">
  <svg class="header-art" viewBox="0 0 860 280" aria-hidden="true">
    <path fill="var(--navy)" d="M0,0 H860 V118 C780,82 700,68 620,72 C520,80 420,180 300,212 C180,242 70,215 0,150 Z"/>
    <path fill="var(--green)" d="M18,160 C90,215 190,232 300,210 C420,182 510,90 620,72 C520,95 430,195 305,222 C190,246 90,220 18,160 Z"/>
    <path fill="var(--navy)" d="M0,150 C60,205 150,235 250,232 C160,246 70,225 0,175 Z"/>
    <path fill="var(--green)" d="M510,130 C600,92 700,80 780,95 C830,108 860,128 860,150 V272 C830,200 760,132 640,120 C590,116 545,120 510,130 Z"/>
  </svg>

  <div class="school-mark">
    <span class="dot"></span>
    <span class="name">Maple Hollow<span class="sub">ELEMENTARY SCHOOL</span></span>
  </div>

  <div class="recipient">
    <span class="to">To</span>
    <span class="name">Nora Whitfield</span>
    CEO, BRIGHTLEAF STUDIO<br>
    <b>W:</b> www.brightleafstudio-example.com
  </div>

  <div class="letter-date"><b>Date:</b> 24-03-2018</div>

  <div class="letter-body">
    <p>Lorem ipsum dolor sit amet, consectetur adipiscing elit. Pellentesque dictum, ante non ullamcorp er convallis, nunc quam blandit metus, ac mollis eros felis a orci. Donec congue, mauris ut pulvinar lobortis, dolor massa feugiat nisi, at tincidunt metus leo vel elit. Proin facilisis semper lobortis. Vivamus augue purus, cursus quis urna non, accumsan pellentesque est. Nulla in iaculis magna, quis aliqu et ex. Cras efficitur metus eget purus euismod facilisis. Proin non metus tincidunt, auctor ipsum a, tempor mi.</p>
    <p class="strong">Nulla egestas vulputate risus, ut vestibulum diam commodo id. Mauris ornare libero eu erat portt itor ultrices. Proin sed lectus scelerisque ligula bibendum sagittis ac nec leo. Donec ac accumsan diam, et lobortis mauris.</p>
    <p class="strong">Nulla congue volutpat nisl ac lobortis. Integer dignissim interdum libero, quis feugiat velit pretium at. Phasellus sit amet libero rutrum, feugiat odio et, tempus purus. Cras ultricies, leo at fringilla solli cit udin, leo sapien placerat enim, a rutrum lorem enim ut tortor. Phasellus magna ante, cong ue maximus egestas sit amet, venenatis scelerisque felis.</p>
    <p>Nulla congue volutpat nisl ac lobortis. Integer dignissim interdum libero, quis feugiat velit pretium at. Phasellus sit amet libero rutrum, feugiat odio et, tempus purus. Cras ultricies, leo at fringilla solli cit udin, leo sapien placerat enim, a rutrum lorem enim ut tortor. Phasellus magna ante, cong ue maximus egestas sit amet, venenatis scelerisque felis.</p>
    <p>Curabitur vitae urna volutpat, varius velit vehicula, fermentum magna. In maximus metus nunc, nec aliquet justo commodo eget. Nullam rhoncus vehicula gravida. Maecenas non sem at erat lacinia con vallis. Aliquam at lobortis erat.</p>
    <p>Nulla congue volutpat nisl ac lobortis. Integer dignissim interdum libero, quis feugiat velit pretium at. Phasellus sit amet libero rutrum, feugiat odio et, tempus purus. Cras ultricies, leo at fringilla solli cit udin, leo sapien placerat enim, a rutrum lorem enim ut tortor. Phasellus magna ante, cong ue maximus egestas sit amet, venenatis scelerisque felis</p>
  </div>

  <div class="sign-off">
    <div class="signature" role="img" aria-label="Handwritten signature of the sender"></div>
    <div class="rule"></div>
    <div class="designation">DESIGNATION PLACE HERE</div>
  </div>

  <svg class="footer-art" viewBox="0 0 860 200" aria-hidden="true">
    <path fill="var(--charcoal)" d="M0,92 C60,32 150,14 250,38 C380,72 480,150 620,162 C720,170 800,150 860,125 V200 H0 Z"/>
    <path fill="var(--green)" d="M18,98 C80,42 160,22 250,38 C380,62 480,140 625,174 C480,152 380,82 250,50 C160,30 80,55 18,98 Z"/>
  </svg>

  <div class="footer-name">Maple Hollow Elementary</div>

  <div class="contact">
    <b>P:</b> (949) 555-0147 &nbsp;|&nbsp; <b>F:</b> (949) 555-0148<br>
    <b>E:</b> info@maplehollow.qpsd-example.org<br>
    <b>W:</b> www.maplehollow.qpsd-example.org<br>
    <span class="address">718 Dovetail Fern, Irvine, CA 92614</span>
  </div>
</div>
</body>
</html>
```